Business Card Design needed for logo design project

Would like a professional business card for a company involved in financial and latest technologies including CAD design. We would like the card to convey professionalism and communicate that we are involved in up to date technology solutions.

Target Market(s)

Business 2 Business sales

Industry/Entity Type

Financial

Colors

Designer to choose colors to be used in the design.

Requirements
Must have
• Business Name
Logo
Name
Phone
Email
Nice to have
• Website

```html
<!DOCTYPE html>
<html lang="en">
<head>
<meta charset="utf-8">
<title>Norvale Business Card</title>
<link rel="stylesheet" href="https://fonts.googleapis.com/css2?family=Jost:wght@400;600;700&display=swap">
<style>
  :root {
    --backdrop: #3b3b3d;
    --card-red: #c8161d;
    --card-red-deep: #9e1016;
    --card-white: #f1f1ef;
    --ink: #1c1c1c;
    --brand-navy: #1f2a5c;
    --brand-white: #ffffff;
  }
  * { box-sizing: border-box; margin: 0; padding: 0; }
  html, body {
    width: 1200px;
    height: 900px;
    overflow: hidden;
    background: var(--backdrop);
    font-family: "Jost", sans-serif;
  }
  .stage {
    width: 1200px;
    height: 900px;
    display: flex;
    align-items: center;
    justify-content: center;
    gap: 60px;
  }
  .card {
    width: 520px;
    height: 300px;
    position: relative;
    box-shadow: 0 10px 24px rgba(0,0,0,0.35);
  }
  .card--front {
    background: radial-gradient(circle at 40% 40%, var(--card-red) 0%, var(--card-red-deep) 100%);
    display: flex;
    align-items: center;
    justify-content: center;
  }
  .brand-name {
    font-weight: 700;
    letter-spacing: 0.06em;
    line-height: 1;
  }
  .card--front .brand-name {
    font-size: 58px;
    color: var(--brand-white);
  }
  .card--back {
    background: var(--card-white);
    color: var(--ink);
    padding: 34px 36px;
  }
  .card--back .brand-name {
    position: absolute;
    top: 30px;
    right: 36px;
    font-size: 34px;
    color: var(--brand-navy);
  }
  .holder-name {
    font-weight: 600;
    font-size: 15px;
  }
  .holder-role {
    font-size: 13px;
    margin-top: 2px;
  }
  .address {
    margin-top: 22px;
    font-size: 13px;
    line-height: 1.45;
  }
  .contact {
    position: absolute;
    left: 36px;
    bottom: 30px;
    font-size: 14px;
    line-height: 1.45;
  }
  .contact .web { margin-bottom: 14px; }
</style>
</head>
<body>
  <main class="stage">
    <section class="card card--front" aria-label="Card front">
      <span class="brand-name">NORVALE</span>
    </section>
    <section class="card card--back" aria-label="Card back">
      <span class="brand-name">NORVALE</span>
      <p class="holder-name">Your Name</p>
      <p class="holder-role">Managing director</p>
      <p class="address">250 Harbor Lane<br>Town State, zip code</p>
      <div class="contact">
        <p class="email">name@norvale.com</p>
        <p class="web">www.norvale.com</p>
        <p class="tel">Tel. +1 555 20 200</p>
        <p class="fax">Fax +1 555 20 200</p>
        <p class="mobile">Mobile +1 555 20 200</p>
      </div>
    </section>
  </main>
</body>
</html>
```